Harbor Mortgage Relief

Please help us give our website a remake or a FACELIFT. It is not very good but it says what we need it to say. But the design is terrible.
I would like our new design font and logo to be used as the theme.

I also want more photos on the site.

I also want consistency with the pages so they look clean.

We want the professionals to do this, let's see what you got!

Thank you!
Updates

Project Deadline Extended
Reason: I can understand you want to be paid. So I will commit to the fee but I want you to have time to make a KICK ASS website for me dudes! Thanks

HI!  Just wanted to say thanks for your time on these.  A lot are great.  However the firefighters have nothing to do with Foreclosure.  We are saving peoples homes from the bank taking them and selling them.   I LOVE the house photos and the families on the website.  That is the direction we like.  THanks.

THANK U ALL FOR THE WORK!   I like a few ending in the numbers: 147  733  693  536  620  478  727  508     I will go over them and choose one soon.  Thank you.   You will be paid shortly. 

Requirements
Must have
• Bright, Upbeat photos. Color scheme should be in order. We like icons on the bottom. not just text.

```html
<!DOCTYPE html>
<html lang="en">
<head>
<meta charset="utf-8">
<title>Harbor Mortgage Relief</title>
<link rel="stylesheet" href="https://fonts.googleapis.com/css2?family=Source+Sans+3:ital,wght@0,400;0,600;0,700;1,400&family=Arimo:wght@400&display=swap">
<style>
:root{
  --red:#e01b1b;
  --ink:#111;
  --text:#222;
  --muted:#8a8a8a;
  --link:#2a7bbf;
  --bar:#f4f4f4;
  --footer:#f2f2f2;
  --rule:#d8d8d8;
  --quote:#a9a9a9;
}
*{margin:0;padding:0;box-sizing:border-box}
html,body{width:1200px;height:1156px;overflow:hidden;background:#fff}
body{position:relative;font-family:"Source Sans 3",sans-serif;color:var(--text)}
.abs{position:absolute}
.topbar{left:0;top:0;width:1200px;height:31px;background:linear-gradient(#fbfbfb,#efefef)}
.topbar span{position:absolute;right:126px;top:9px;font-size:11px;color:var(--ink)}
.brand{left:132px;top:46px;display:flex;align-items:center;gap:12px}
.brand-dot{width:66px;height:66px;border-radius:50%;background:var(--red)}
.brand-name{font-weight:700;font-size:19px;line-height:19px;color:var(--red);width:160px;text-transform:uppercase}
.phone{right:125px;top:48px;font-size:25px;color:var(--ink);display:flex;align-items:center;gap:5px}
.nav{right:126px;top:94px;font-size:11.5px;color:#444;display:flex;gap:7px}
.nav .on{color:var(--red)}
.nav i{font-style:normal;color:#777}
.hero{left:126px;top:129px;width:949px;height:364px;background:linear-gradient(180deg,#e9ecee 0%,#d8dbdc 45%,#7aa34a 78%,#4f7f2b 100%)}
.hero-photo{position:absolute;right:0;top:0;width:400px;height:364px;background:linear-gradient(160deg,#c9ccd0,#b89a85 45%,#6f8fb4 75%,#5a7f3a)}
.hero h1{position:absolute;left:20px;top:116px;font-size:25px;line-height:30px;font-weight:600;color:var(--ink)}
.btn{position:absolute;left:17px;top:199px;width:140px;height:27px;border-radius:14px;background:var(--red);border:2px solid #fff;box-shadow:0 0 0 1px #c91515;color:#fff;font-size:13px;display:flex;align-items:center;justify-content:center;gap:8px}
.swoosh{left:0;top:380px}
.welcome{left:127px;top:515px;width:650px}
.welcome h2,.news h2{font-size:19.5px;font-weight:400;color:var(--ink);margin-bottom:3px}
.welcome p{font-family:"Arimo",sans-serif;font-size:10.1px;line-height:12.2px;color:var(--ink);margin-bottom:12px}
.divider{left:808px;top:523px;height:230px;border-left:1px dotted #bbb}
.news{left:848px;top:515px;width:220px}
.news .sub{font-family:"Arimo",sans-serif;font-size:8.5px;font-style:italic;color:var(--muted);margin-bottom:14px}
.item{display:flex;gap:12px;padding-bottom:10px;margin-bottom:16px;border-bottom:1px solid #ccc;font-family:"Arimo",sans-serif}
.item:last-child{border:none}
.date{width:36px;height:40px;flex:none;border-radius:3px;box-shadow:0 1px 2px #aaa;overflow:hidden;text-align:center}
.date b{display:block;background:#8cc43f;color:#fff;font-size:8px;font-weight:400;height:13px;line-height:13px}
.date span{display:block;font-size:17px;color:#2a8fc8;line-height:26px;background:#f6f6f6}
.item h3{font-size:10px;font-weight:400;color:var(--ink);margin-bottom:4px}
.item p{font-size:8.5px;line-height:15px;color:#333}
.item a{display:block;text-align:right;color:var(--link);font-size:8.5px;font-weight:700;text-decoration:none;margin-top:4px;margin-right:30px}
.arrow{top:818px;font-size:40px;font-weight:300;color:#666}
.t-photo{left:194px;top:782px;width:152px;height:114px;border:1px solid #ccc;padding:5px;background:#fff;box-shadow:0 6px 6px -4px #bbb}
.t-photo div{width:100%;height:100%;background:linear-gradient(160deg,#c5cad0,#b58f78 50%,#5f86b0 80%,#4d7a33)}
.quote{left:368px;top:793px;width:630px;font-style:italic;font-size:16.5px;line-height:20px;color:var(--quote)}
.quote .mark{font-size:38px;font-style:normal;color:#ccc;vertical-align:-14px;line-height:0}
.quote .who{display:block;margin-top:14px;font-size:16px}
.footer{left:6px;top:933px;width:1189px;height:223px;background:var(--footer)}
.fcol{top:951px;font-size:11px}
.fcol h4{font-weight:600;font-size:11.5px;color:var(--ink);margin-bottom:6px}
.fline{display:flex;gap:6px;align-items:flex-start;font-size:9.5px;font-weight:600;color:#222;margin-bottom:12px;line-height:12px}
.social{display:flex;align-items:center;gap:10px;font-size:9.5px;font-weight:600;color:#222;margin-bottom:7px}
.social i{width:30px;height:30px;border-radius:4px;background:linear-gradient(#5b9bd5,#2f6fa8);display:block}
.flinks{left:872px;top:950px;list-style:none}
.flinks li{font-size:12px;font-weight:600;color:#222;height:20.3px;padding-left:15px;position:relative}
.flinks li.on::before{content:"→";position:absolute;left:0;top:-1px;color:var(--red);font-size:11px}
.frule{left:198px;top:1093px;width:794px;border-top:1px solid #cfcfcf}
.legal{left:180px;top:1103px;width:840px;text-align:center;font-size:9px;line-height:12.5px;color:#666}
.legal .c{font-size:11px;color:#888}
</style>
</head>
<body>
<div class="abs topbar"><span>Hablamos Espanol</span></div>

<div class="abs brand"><div class="brand-dot"></div><div class="brand-name">Harbor Mortgage Relief</div></div>

<div class="abs phone">
  <svg width="20" height="16" viewBox="0 0 20 16"><path d="M1 5c0-3 4-4 9-4s9 1 9 4l-4 1-1-2H6L5 6z" fill="#e01b1b"/><rect x="3" y="7" width="14" height="8" rx="1" fill="#e01b1b"/><circle cx="10" cy="11" r="2" fill="#fff"/></svg>
  888-555-0142
</div>

<nav class="abs nav"><span class="on">Home</span><i>/</i><span>About Us</span><i>/</i><span>Services</span><i>/</i><span>Contact Us</span><i>/</i><span>Financing Options</span></nav>

<section class="abs hero" role="img" aria-label="Smiling family lying on the lawn in front of their house">
  <div class="hero-photo"></div>
  <h1>Bringing your mortgage current<br>to stop the foreclosure</h1>
  <div class="btn">Go to Services
    <svg width="14" height="10" viewBox="0 0 14 10"><path d="M1 5h11M8 1l4 4-4 4" stroke="#fff" stroke-width="2" fill="none"/></svg>
  </div>
</section>

<svg class="abs swoosh" width="1200" height="150" viewBox="0 380 1200 150">
  <path d="M32 523Q600 393 1172 523L1172 530L32 530Z" fill="#fff"/>
  <path d="M32 523Q600 351 1172 523Q600 393 32 523Z" fill="var(--red)"/>
  <circle cx="577" cy="448" r="5" fill="#111"/>
  <circle cx="594" cy="448" r="5" fill="#fff"/>
  <circle cx="611" cy="448" r="5" fill="#fff"/>
  <circle cx="628" cy="448" r="5" fill="#fff"/>
</svg>

<section class="abs welcome">
  <h2>Welcome to our Website</h2>
  <p>HARBOR MORTGAGE RELIEF specializes in assisting homeowners who are in FORECLOSURE, by offering solid alternatives to losing your home in a Trustee Sale. Having your home foreclosed on can damage your credit for up to 7 years. Most foreclosures end with the home owner being evicted from their home, leaving them with no money, no place to live and without ample time to safely remove their possessions from their home. There is no need to have this happen to you. No matter what part of foreclosure process you are in, WE CAN HELP!<br>If you have received a Notice of Default (NOD) or Notice of Trustee Sale (NTS), you have options. Contact us today to speak to one of our licensed specialist, and let us help you put this situation behind you.</p>
  <p>We speak to hundreds of homeowners every day, we understand how frustrating this can be. Don't live in fear of what is to come. You have other options, please call or email us today and we will immediately put our specialist to work finding you a solution.</p>
  <p>Don't try to handle this frustrating situation by yourself. HARBOR MORTGAGE RELIEF is a team of knowledgeable real estate professionals, we can offer you a better solution during this tough time.</p>
  <p>HARBOR MORTGAGE RELIEF has been assisting families in foreclosure for years. Our skill and integrity has earned us a reputation for fast, professional, courteous and thorough solutions. With over 50 years of real estate knowledge and experience HARBOR MORTGAGE RELIEF is ready to assist you.</p>
</section>

<div class="abs divider"></div>

<aside class="abs news">
  <h2>Latest News/Events:</h2>
  <div class="sub">Lorem ipsum dolor sit amet, consectetur.</div>
  <div class="item">
    <div class="date"><b>NOV</b><span>05</span></div>
    <div><h3>Lorem Ipsum dolor sit amet</h3><p>Lorem Ipsum is simply dummy text of the printing and typesetting industry.</p><a>Read More</a></div>
  </div>
  <div class="item">
    <div class="date"><b>NOV</b><span>05</span></div>
    <div><h3>Lorem Ipsum dolor sit amet</h3><p>Lorem Ipsum is simply dummy text of the printing and typesetting industry.</p><a>Read More</a></div>
  </div>
</aside>

<div class="abs arrow" style="left:148px">&#10216;</div>
<div class="abs arrow" style="left:1030px">&#10217;</div>
<div class="abs t-photo"><div role="img" aria-label="Photo of a happy family outside their home"></div></div>
<blockquote class="abs quote">
  <span class="mark">&ldquo;</span> I'd like to express my gratitude to you and your company and I have to add, for all of the trustworthy and reliable service that you bring to the public. Your company helped put me back together, you in particular are awesome! Thank you again Ray. <span class="mark">&rdquo;</span>
  <span class="who">Dolores</span>
</blockquote>

<footer class="abs footer"></footer>

<div class="abs fcol" style="left:210px">
  <h4>Contact Us:</h4>
  <div class="fline"><svg width="13" height="10" viewBox="0 0 20 16"><path d="M1 5c0-3 4-4 9-4s9 1 9 4l-4 1-1-2H6L5 6z" fill="#e01b1b"/><rect x="3" y="7" width="14" height="8" rx="1" fill="#e01b1b"/></svg>888-555-0142</div>
  <div class="fline"><svg width="12" height="12" viewBox="0 0 12 12"><circle cx="6" cy="6" r="5" fill="none" stroke="#e01b1b"/><path d="M1 6h10M6 1v10M3 2.5q3 3.5 0 7M9 2.5q-3 3.5 0 7" stroke="#e01b1b" fill="none" stroke-width=".8"/></svg>info@harbormortgagerelief.com</div>
  <div class="fline"><svg width="16" height="11" viewBox="0 0 16 11"><rect width="16" height="11" fill="#e01b1b"/><path d="M0 0l8 6 8-6" stroke="#fff" fill="none"/></svg><span>118 Harbor Street<br>Suite 210, Bayview,<br>CA 90000</span></div>
</div>

<div class="abs fcol" style="left:553px">
  <h4>Connect With Us:</h4>
  <div class="social"><i></i>Find us on Friendbook</div>
  <div class="social"><i></i>Tweet us on Chirper</div>
  <div class="social"><i></i>Share your thoughts on Linkly</div>
</div>

<ul class="abs flinks">
  <li class="on">Home</li><li>About Us</li><li>Services</li><li>Contact Us</li><li>Financing Options</li>
</ul>

<div class="abs frule"></div>
<div class="abs legal">
  <div class="c">© Harbor Mortgage Relief 2012 | All Rights Reserved.</div>
  Lorem Ipsum is simply dummy text of the printing and typesetting industry. Lorem Ipsum has been the industry's standard dummy text ever since the 1500s, when an unknown printer took a galley of type and scrambled it to make a type specimen book.
</div>
</body>
</html>
```